Customs House descriptive business cards

We require a two-sided business card that has a simple yet elegant design. We want to be able to promote our services as a customs house. This card should include our logo, contact info and services offered with the logo being on one side and the contact info and services on the flip side

Target Market(s)

Importers / exporters to and from the Bahamas

Industry/Entity Type

Logistics

Contact Information for Business Card

The front side of the card could have the logo and the flip side should have the other relevant info

Font styles to use
Serif

Colors

Designer to choose colors to be used in the design.

Requirements
Must have
• (Harbourline Agents Ltd) Logo, address and contact info also services:
• import customs clearance, Delivery & HAndling services,Florida pickups, Export packing & Crating Services, export customs clearance, Consulting

```html
<!DOCTYPE html>
<html lang="en">
<head>
<meta charset="utf-8">
<title>Harbourline Agents Ltd — Business Card</title>
<link rel="stylesheet" href="https://fonts.googleapis.com/css2?family=Tinos:wght@400;700&family=Arimo:wght@400&display=swap">
<style>
  :root{
    --bg:#2b2b2d;
    --card:#ffffff;
    --brand-blue:#1f63b8;
    --light-blue:#3b8fd6;
    --grey:#a9a9ab;
    --text-dark:#1b3f73;
  }
  *{margin:0;padding:0;box-sizing:border-box}
  html,body{width:1200px;height:904px;overflow:hidden;background:var(--bg)}
  .canvas{position:relative;width:1200px;height:904px}
  .card{
    position:absolute;left:220px;width:760px;height:420px;
    background:var(--card);border-radius:22px;overflow:hidden;
    box-shadow:0 10px 24px rgba(0,0,0,.45);
  }
  .card--front{top:20px}
  .card--back{top:464px}

  /* wordmark */
  .wordmark{display:flex;align-items:center;gap:14px}
  .wordmark__dot{width:30px;height:30px;border-radius:50%;background:var(--light-blue);flex:none}
  .wordmark__name{
    font-family:"Tinos",serif;font-weight:700;color:var(--brand-blue);
    letter-spacing:1px;text-transform:uppercase;line-height:1;
  }

  /* front */
  .front__logo{position:absolute;left:0;right:0;top:120px;display:flex;justify-content:center}
  .front__logo .wordmark__name{font-size:40px}
  .services{
    position:absolute;left:60px;right:60px;top:232px;text-align:center;
    font-family:"Arimo",sans-serif;font-size:17px;line-height:1.55;color:var(--brand-blue);
  }
  .services .sep{display:inline-block;width:7px;height:7px;border-radius:50%;background:var(--brand-blue);margin:0 6px;vertical-align:middle}

  /* back */
  .back__logo{position:absolute;left:40px;top:175px;width:370px}
  .back__logo .wordmark__name{font-size:27px}
  .back__divider{position:absolute;left:440px;top:55px;width:1.5px;height:225px;background:var(--light-blue)}
  .contact{position:absolute;left:470px;top:52px;font-family:"Tinos",serif;color:var(--text-dark)}
  .contact__name{font-size:22px;font-weight:700;color:var(--brand-blue);text-transform:uppercase;letter-spacing:.5px}
  .contact__role{font-size:14px;color:var(--grey);text-transform:uppercase;letter-spacing:1.5px;margin-bottom:10px}
  .contact__row{display:flex;align-items:center;gap:10px;font-size:16px;line-height:1.55}
  .contact__row svg{width:14px;height:14px;flex:none}
  .contact__address{font-size:16px;line-height:1.5;margin-top:8px;padding-left:24px}
  .social{position:absolute;right:40px;top:300px;display:flex;align-items:center;gap:12px;
    font-family:"Tinos",serif;font-size:15px;font-weight:700;color:var(--brand-blue);letter-spacing:.5px}
  .social__dot{width:18px;height:18px;border-radius:50%;border:2px solid var(--brand-blue)}
  .back__rule{position:absolute;left:40px;right:40px;top:345px;height:1.5px;background:var(--brand-blue)}
</style>
</head>
<body>
<div class="canvas">

  <section class="card card--front">
    <div class="front__logo">
      <div class="wordmark"><span class="wordmark__dot"></span><span class="wordmark__name">Harbourline Agents Ltd</span></div>
    </div>
    <p class="services">
      Import customs clearance<span class="sep"></span>Delivery &amp; HAndling services<br>
      Florida pickups Export packing &amp; Crating Services<span class="sep"></span>export customs clearance<br>
      Consulting
    </p>
  </section>

  <section class="card card--back">
    <div class="back__logo">
      <div class="wordmark"><span class="wordmark__dot"></span><span class="wordmark__name">Harbourline Agents Ltd</span></div>
    </div>
    <div class="back__divider"></div>
    <div class="contact">
      <div class="contact__name">Marcus Elliott</div>
      <div class="contact__role">Operations Director</div>
      <div class="contact__row">
        <svg viewBox="0 0 16 16"><path d="M3 1l3 3-1.5 2a9 9 0 005.5 5.5L12 10l3 3-2 2C7 15 1 9 1 3z" fill="#3b8fd6"/></svg>
        (242) 555-0140 (Office)</div>
      <div class="contact__row">
        <svg viewBox="0 0 16 16"><path d="M3 1l3 3-1.5 2a9 9 0 005.5 5.5L12 10l3 3-2 2C7 15 1 9 1 3z" fill="#3b8fd6"/></svg>
        (242) 555-0172 (Cell)</div>
      <div class="contact__row">
        <svg viewBox="0 0 16 16" fill="none" stroke="#3b8fd6" stroke-width="1.4"><circle cx="8" cy="8" r="6.5"/><ellipse cx="8" cy="8" rx="3" ry="6.5"/><path d="M1.5 8h13"/></svg>
        www.harbourlineagents.com</div>
      <div class="contact__row">
        <svg viewBox="0 0 16 16"><rect x="1" y="3" width="14" height="10" fill="#3b8fd6"/><path d="M1 3l7 6 7-6" fill="none" stroke="#fff" stroke-width="1.3"/></svg>
        imports@harbourlineagents.com</div>
      <div class="contact__address">
        #42 Seagrape Lane<br>P.O Box SP-40217<br>Nassau, Bahamas
      </div>
    </div>
    <div class="social">FIND US ON <span class="social__dot"></span><span class="social__dot"></span></div>
    <div class="back__rule"></div>
  </section>

</div>
</body>
</html>
```